We are a building company that build new homes and units we are looking for something fresh and looks good my company name is
Larkmoor Building Group Pty Ltd

Industry/Entity Type

Building

Contact Information for Business Card

Name Marco Delacruz-Fenn
Tittle: Director
Address 14 Quarrel St. Thornbury Vic 3071
Ph: 03 9612 4087
Mobile : 0400 562 938

www.larkmoorbuildinggroup.com.au
Email: sales@larkmoorbuildinggroup.com.au

```html
<!DOCTYPE html>
<html lang="en">
<head>
<meta charset="utf-8">
<title>Larkmoor Building Group – Business Card</title>
<link rel="stylesheet" href="https://fonts.googleapis.com/css2?family=Open+Sans:wght@400;600;700&display=swap">
<style>
  :root {
    --stage-top: #c9c9c9;
    --stage-bottom: #8c8c8c;
    --brand-blue: #2b3a8c;
    --accent-blue: #3142a6;
    --stripe-silver: #c7c9d6;
    --card-white: #ffffff;
    --card-black: #101114;
    --card-charcoal: #1c1d22;
    --text-light: #f2f2f2;
    --text-dark: #1a1a1a;
    --silver: #d9dce6;
  }
  * { box-sizing: border-box; margin: 0; padding: 0; }
  html, body {
    width: 1200px; height: 900px; overflow: hidden;
  }
  body {
    background: linear-gradient(180deg, var(--stage-top) 0%, #b3b3b3 45%, var(--stage-bottom) 100%);
    font-family: "Open Sans", Arial, sans-serif;
    position: relative;
  }
  .card {
    position: absolute;
    top: 300px;
    width: 520px;
    height: 300px;
    border-radius: 22px;
    overflow: hidden;
    box-shadow: 0 18px 30px rgba(0,0,0,0.35);
  }
  .card-front { left: 50px; background: var(--card-black); }
  .card-back {
    left: 630px;
    background: linear-gradient(160deg, var(--card-charcoal) 0%, var(--card-black) 70%);
  }

  /* Front */
  .front-top {
    position: absolute; left: 0; top: 0; width: 100%; height: 168px;
    background: var(--card-white);
  }
  .front-building-visual {
    position: absolute; right: 0; top: 0; width: 150px; height: 168px;
    background: linear-gradient(100deg, rgba(255,255,255,0) 0%, rgba(200,205,220,0.55) 45%, rgba(170,176,196,0.6) 100%);
  }
  .brand-stripe {
    position: absolute; left: 0; top: 168px; width: 100%; height: 14px;
    background: linear-gradient(180deg, var(--accent-blue) 0 55%, var(--stripe-silver) 55% 100%);
  }
  .brand-lockup {
    position: absolute; left: 28px; top: 46px;
    display: flex; align-items: center; gap: 12px;
  }
  .brand-mark {
    width: 42px; height: 42px; background: var(--brand-blue);
  }
  .brand-name {
    color: var(--brand-blue);
    font-weight: 700;
    font-size: 21px;
    line-height: 1.15;
    width: 230px;
  }
  .holder {
    position: absolute; right: 26px; top: 24px; text-align: right;
  }
  .holder-name {
    color: var(--brand-blue); font-weight: 700; font-size: 17px;
  }
  .holder-title {
    color: var(--text-dark); font-size: 12px; margin-top: 2px;
  }
  .contact-list {
    position: absolute; left: 24px; top: 198px;
    list-style: none; color: var(--text-light);
    font-size: 13px; line-height: 17px;
  }
  .contact-list li { display: flex; align-items: center; gap: 6px; }
  .contact-list svg { width: 12px; height: 12px; fill: #9aa0b8; flex: none; }

  /* Back */
  .back-building-visual {
    position: absolute; right: 0; top: 0; width: 150px; height: 300px;
    background: linear-gradient(90deg, rgba(255,255,255,0) 0%, rgba(255,255,255,0.05) 60%, rgba(255,255,255,0.08) 100%);
  }
  .back-lockup {
    position: absolute; left: 0; right: 0; top: 112px;
    display: flex; justify-content: center; align-items: center; gap: 14px;
  }
  .back-lockup .brand-mark { background: var(--accent-blue); width: 48px; height: 48px; }
  .back-lockup .brand-name { color: var(--silver); font-size: 23px; width: 260px; }
</style>
</head>
<body>

<section class="card card-front" aria-label="Business card front">
  <div class="front-top"></div>
  <div class="front-building-visual" role="img" aria-label="Faint photo of a glass building facade"></div>
  <div class="brand-lockup">
    <span class="brand-mark"></span>
    <span class="brand-name">Larkmoor Building Group Pty Ltd</span>
  </div>
  <div class="holder">
    <div class="holder-name">Marco Delacruz-Fenn</div>
    <div class="holder-title">Director</div>
  </div>
  <div class="brand-stripe"></div>
  <ul class="contact-list">
    <li><svg viewBox="0 0 12 12"><rect x="3" y="0.5" width="6" height="11" rx="1"/></svg>0400 562 938</li>
    <li><svg viewBox="0 0 12 12"><path d="M2.5 1 L4.5 1 L5.3 3.6 L4 4.6 C4.7 6.2 5.8 7.3 7.4 8 L8.4 6.7 L11 7.5 L11 9.5 C11 10.3 10.3 11 9.5 11 C5 11 1 7 1 2.5 C1 1.7 1.7 1 2.5 1Z"/></svg>03 9612 4087</li>
    <li><svg viewBox="0 0 12 12"><circle cx="6" cy="6" r="5.2" fill="none" stroke="#9aa0b8" stroke-width="1.2"/><path d="M1 6H11M6 1C3.5 4 3.5 8 6 11M6 1C8.5 4 8.5 8 6 11" fill="none" stroke="#9aa0b8" stroke-width="1"/></svg>www.larkmoorbuildinggroup.com.au</li>
    <li><svg viewBox="0 0 12 12"><rect x="0.5" y="2" width="11" height="8" rx="1"/><path d="M1 2.6 L6 6.5 L11 2.6" fill="none" stroke="#101114" stroke-width="1"/></svg>sales@larkmoorbuildinggroup.com.au</li>
    <li><svg viewBox="0 0 12 12"><path d="M6 0.8 L11.5 5.8 H9.8 V11 H7.2 V7.6 H4.8 V11 H2.2 V5.8 H0.5Z"/></svg>14 Quarrel St. Thornbury Vic 3071</li>
  </ul>
</section>

<section class="card card-back" aria-label="Business card back">
  <div class="back-building-visual" role="img" aria-label="Faint photo of a building facade"></div>
  <div class="back-lockup">
    <span class="brand-mark"></span>
    <span class="brand-name">Larkmoor Building Group Pty Ltd</span>
  </div>
</section>

</body>
</html>
```